Letterhead Design Needed for Real Estate Office

We are a boutique real estate agency focused on property management. We need a letter head which is professional looking and include the following information:

Logo
ABN Number
Address
Postal Address
Phone
Fax
Mobile
Email
Website

Please note that the PLVAQT logo can not be changed and must be positioned at the bottom right corner.

Please find attached the existing letterhead design for all the required elements.

Target Market(s)

Letterhead mostly used for service of notices, business letters, clients communication

Industry/Entity Type

Boutique

Colors

Designer to choose colors to be used in the design.

Requirements
Must have
• Logo

```html
<!DOCTYPE html>
<html lang="en">
<head>
<meta charset="utf-8">
<title>Crestfield Partners Letterhead</title>
<link href="https://fonts.googleapis.com/css2?family=Open+Sans:wght@400;700&family=Roboto+Condensed:wght@400&display=swap" rel="stylesheet">
<style>
  :root {
    --brand-green: #78a843;
    --ink: #231f20;
    --paper: #ffffff;
    --partner-blue: #1a5aa6;
  }
  html, body {
    margin: 0;
    padding: 0;
    overflow: hidden;
    background: var(--paper);
  }
  .letterhead {
    position: relative;
    width: 927px;
    height: 1200px;
    background: var(--paper);
    overflow: hidden;
    font-family: "Open Sans", Arial, sans-serif;
    color: var(--ink);
  }
  .side-band {
    position: absolute;
    left: 0;
    top: 0;
    width: 109px;
    height: 1200px;
    background: var(--brand-green);
  }
  .contact-list {
    position: absolute;
    left: 139px;
    top: 38px;
    margin: 0;
    padding: 0;
    list-style: none;
    font-size: 15.5px;
    line-height: 20.5px;
  }
  .contact-list .label {
    display: inline-block;
    width: 20px;
    color: var(--brand-green);
  }
  .brand-name {
    position: absolute;
    right: 24px;
    top: 58px;
    display: flex;
    align-items: center;
    gap: 14px;
    font-weight: 700;
    font-size: 30px;
    letter-spacing: 0.5px;
    color: var(--ink);
  }
  .brand-name .brand-square {
    width: 40px;
    height: 40px;
    background: var(--brand-green);
  }
  .member-badge {
    position: absolute;
    right: 24px;
    top: 1074px;
    display: flex;
    align-items: center;
    gap: 10px;
    font-weight: 700;
    font-size: 30px;
    color: var(--partner-blue);
  }
  .member-badge .badge-square {
    width: 30px;
    height: 30px;
    background: var(--partner-blue);
  }
  .footer-line {
    position: absolute;
    left: 116px;
    top: 1133px;
    margin: 0;
    font-family: "Roboto Condensed", "Arial Narrow", sans-serif;
    font-size: 11.5px;
    white-space: nowrap;
    color: var(--ink);
  }
</style>
</head>
<body>
  <div class="letterhead">
    <div class="side-band"></div>

    <ul class="contact-list">
      <li><span class="label">F</span>9420 6177</li>
      <li><span class="label">M</span>0477 352 610</li>
      <li><span class="label">P</span>9413 5260</li>
      <li><span class="label">W</span>www.crestfieldre.cc</li>
    </ul>

    <div class="brand-name">
      <span class="brand-square"></span>
      <span>Crestfield Partners</span>
    </div>

    <div class="member-badge">
      <span class="badge-square"></span>
      <span>PLVAQT</span>
    </div>

    <p class="footer-line">ABN 42 608 315 729 | Shop 12B 215-229 Harbour Parade Linfield NSW 2071 AUSTRALIA | PO BOX 514 LINFIELD NSW 2071</p>
  </div>
</body>
</html>
```